Korlane Email Signature Banners – Fabrication Capability Series

www.Korlane.com.au is an Australian engineering and fabrication company specialising in fabrication and welding of :
steel piping spools,
skids and frames,
small volume process steel tanks
and general steel fabrication
We require four distinct banner designs for use in Velnor Tidmark email signatures. Each banner will highlight a specific capability while maintaining a consistent brand identity.
Deliverables
Four banners total:
Piping Spools Fabrication – focus on precision welding and stainless steel pipework
Skid & Frames Fabrication – highlight skid systems and structural frames
Small Steel Tanks Fabrication – show fabricated tanks and workshop craftsmanship
General Fabrication Solutions – broad steel fabrication theme for company-wide use
Dimensions: 600–700 px wide × 100 px high
Format: PNG (preferred), small file size prefered
Resolution: 72 dpi
Background: non-transparent, industrial or workshop setting
Text examples:
1. Piping Spools Fabrication
Option A: “Expert Fabrication Solutions for Process Piping”
Option B: “Precision Welding for Complex Systems”
Option C: “Delivering Quality in Every Spool”
Option D: “Engineered for Flow, Built for Strength”
2. Skid & Frames Fabrication
Option A: “Custom Engineered Modular Systems”
Option B: “Built Strong. Designed Smart.”
Option C: “Reliable Frames for Industrial Performance”
Option D: “Modular Fabrication for Seamless Integration”
3. Small Steel Tanks Fabrication
Option A: “Precision Built for Your Needs”
Option B: “Compact Strength. Proven Durability.”
Option C: “Fabricated for Performance and Longevity”
Option D: “Small Tanks. Big Reliability.”
4. General Fabrication Solutions
Option A: “Quality Craftsmanship, Proven Results”
Option B: “Your Partner in Precision Fabrication”
Option C: “Engineering Excellence in Every Weld”
Option D: “Australian Fabrication. Global Standards.”
Style Direction
Clean, professional, and engineering‑focused
Use Korlane brand colours
Blend photo realism with vector clarity (no heavy gradients)
Include subtle industrial textures or workshop imagery
Typography: bold sans‑serif, legible at small scale
Usage Context
These banners will appear at the bottom of staff email signatures via Tidmark Email Signature Tool for Velnor 365, so clarity and fast loading are essential. No Logo is required in the banners.
Reference
Existing Korlane signature is attached. Colour palette to match the signature style and logo.
Target Market(s)
Engineering and construction companies,
Industry/Entity Type
Engineering fabrication design
Look and feel

```html
<!DOCTYPE html>
<html lang="en">
<head>
<meta charset="utf-8">
<title>Korlane Email Signature Banners</title>
<link href="https://fonts.googleapis.com/css2?family=Poppins:ital,wght@1,800&family=Roboto:wght@700&display=swap" rel="stylesheet">
<style>
  :root {
    --page-bg: #adbdc5;
    --steel-dark: #2d2d30;
    --brand-blue: #29a9e1;
    --headline-blue: #2cb9f2;
    --stripe-grey: #9a9b9d;
    --body-text: #3c3c3e;
    --white: #ffffff;
  }
  html, body {
    margin: 0;
    width: 1200px;
    height: 938px;
    overflow: hidden;
    background: var(--page-bg);
  }
  .banner {
    position: absolute;
    left: 150px;
    width: 878px;
    height: 146px;
    background: var(--white);
    overflow: hidden;
    box-shadow: 0 6px 10px rgba(40, 55, 65, 0.28);
  }
  .banner--spools  { top: 84px; }
  .banner--skids   { top: 290px; }
  .banner--tanks   { top: 497px; }
  .banner--general { top: 703px; }
  .banner__shapes {
    position: absolute;
    inset: 0;
    width: 100%;
    height: 100%;
  }
  .headline {
    position: absolute;
    inset: 0;
    margin: 0;
    font-family: "Poppins", sans-serif;
    font-style: italic;
    font-weight: 800;
    letter-spacing: -1.5px;
    white-space: nowrap;
  }
  .headline__line {
    position: absolute;
    line-height: 1;
  }
  .headline__line--accent { color: var(--headline-blue); }
  .headline__line--solid  { color: var(--white); }
  .tagline {
    position: absolute;
    margin: 0;
    font-family: "Roboto", sans-serif;
    font-weight: 700;
  }
  .tagline--dark  { color: var(--body-text); }
  .tagline--light { color: var(--white); }
  .brand-name {
    position: absolute;
    margin: 0;
    font-family: "Roboto", sans-serif;
    font-weight: 700;
    font-size: 30px;
    line-height: 1;
    color: var(--brand-blue);
    letter-spacing: 0.5px;
    white-space: nowrap;
    transform: translate(-50%, -50%);
  }
</style>
</head>
<body>

<svg width="0" height="0" style="position:absolute">
  <defs>
    <linearGradient id="workshop-tone" x1="0" y1="0" x2="1" y2="1">
      <stop offset="0" stop-color="#3a3b3f"/>
      <stop offset="0.55" stop-color="#2b2b2e"/>
      <stop offset="1" stop-color="#232325"/>
    </linearGradient>
  </defs>
</svg>

<!-- Piping spools -->
<section class="banner banner--spools">
  <svg class="banner__shapes" viewBox="0 0 878 146" preserveAspectRatio="none">
    <polygon role="img" aria-label="Workshop photo of welded stainless steel pipe spools" points="213,0 673,0 637,146 174,146" fill="url(#workshop-tone)"/>
    <polygon points="685,0 696,0 657,146 648,146" fill="var(--steel-dark)"/>
    <polygon points="702,0 714,0 687,108 677,108" fill="var(--stripe-grey)"/>
  </svg>
  <p class="brand-name" style="left:92px; top:73px;">Korlane</p>
  <h2 class="headline">
    <span class="headline__line headline__line--accent" style="left:222px; top:21px; font-size:58px;">PIPING SPOOLS</span>
    <span class="headline__line headline__line--solid" style="left:251px; top:73px; font-size:54px;">FABRICATION</span>
  </h2>
  <p class="tagline tagline--dark" style="left:719px; top:15px; font-size:22px; line-height:22.8px; width:158px;">Focus on precision welding and stainless steel pipework</p>
</section>

<!-- Skid & frames -->
<section class="banner banner--skids">
  <svg class="banner__shapes" viewBox="0 0 878 146" preserveAspectRatio="none">
    <polygon role="img" aria-label="Workshop photo of fabricated steel skids and structural frames" points="0,0 468,0 431,146 0,146" fill="url(#workshop-tone)"/>
    <polygon points="477,0 487,0 450,146 440,146" fill="var(--steel-dark)"/>
    <polygon points="495,0 504,0 480,97 471,97" fill="var(--stripe-grey)"/>
  </svg>
  <h2 class="headline">
    <span class="headline__line headline__line--accent" style="left:18px; top:24px; font-size:56px;">SKID &amp; FRAMES</span>
    <span class="headline__line headline__line--solid" style="left:51px; top:75px; font-size:54px;">FABRICATION</span>
  </h2>
  <p class="tagline tagline--dark" style="left:514px; top:14px; font-size:25.5px; line-height:31px; width:170px;">Highlight skid systems and structural frames</p>
  <p class="brand-name" style="left:766px; top:73px;">Korlane</p>
</section>

<!-- Small steel tanks -->
<section class="banner banner--tanks">
  <svg class="banner__shapes" viewBox="0 0 878 146" preserveAspectRatio="none">
    <polygon role="img" aria-label="Workshop photo of fabricated small steel process tanks" points="0,0 468,0 431,146 0,146" fill="url(#workshop-tone)"/>
    <polygon points="477,0 487,0 450,146 440,146" fill="var(--steel-dark)"/>
    <polygon points="495,0 504,0 480,97 471,97" fill="var(--stripe-grey)"/>
    <polygon points="701,0 712,0 693,97 684,97" fill="var(--brand-blue)"/>
    <polygon points="719,0 878,0 878,146 663,146" fill="var(--brand-blue)"/>
  </svg>
  <h2 class="headline">
    <span class="headline__line headline__line--accent" style="left:26px; top:28px; font-size:41px; letter-spacing:-1px;">SMALL STEEL TANKS</span>
    <span class="headline__line headline__line--solid" style="left:27px; top:64px; font-size:57px;">FABRICATION</span>
  </h2>
  <p class="brand-name" style="left:583px; top:75px;">Korlane</p>
  <p class="tagline tagline--light" style="left:719px; top:11px; font-size:21.3px; line-height:24.4px; width:148px;">Show fabricated tanks and workshop craftsmanship</p>
</section>

<!-- General fabrication -->
<section class="banner banner--general">
  <svg class="banner__shapes" viewBox="0 0 878 146" preserveAspectRatio="none">
    <polygon role="img" aria-label="Workshop photo of general steel fabrication and welding" points="0,0 393,0 354,146 0,146" fill="url(#workshop-tone)"/>
    <polygon points="405,0 416,0 377,146 366,146" fill="var(--steel-dark)"/>
    <polygon points="420,0 432,0 407,98 396,98" fill="var(--stripe-grey)"/>
    <polygon points="654,0 666,0 645,98 636,98" fill="var(--brand-blue)"/>
    <polygon points="672,0 878,0 878,146 615,146" fill="var(--brand-blue)"/>
  </svg>
  <h2 class="headline">
    <span class="headline__line headline__line--accent" style="left:33px; top:10px; font-size:46px;">GENERAL</span>
    <span class="headline__line headline__line--accent" style="left:33px; top:47px; font-size:46px;">FABRICATION</span>
    <span class="headline__line headline__line--solid" style="left:33px; top:85px; font-size:46px;">SOLUTIONS</span>
  </h2>
  <p class="brand-name" style="left:510px; top:75px;">Korlane</p>
  <p class="tagline tagline--light" style="left:690px; top:9px; font-size:22.5px; line-height:24.4px; width:160px;">Broad steel fabrication theme for company-wide use</p>
</section>

</body>
</html>
```